Hip surgeon needs a educative book cover design

I need to re-design my old book cover for its 3rd edition.
It's a small book dedicated to my patients, who underwent total hip replacement. It's meant to help people getting around the basic care after a total hip replacement surgery and getting back to their normal, active life.
The title is: "Walking anew: a gentle recovery companion".
I already had a new logo, new stationery and new website design from ArtisanHive (please see the attachments).
The final design should be look alike the other fresh new designs. It must communicate health, peacefulness.
I also attached the manual as it looks today for reference.
A5 size.
Just cover and back cover.

```html
<!DOCTYPE html>
<html lang="en">
<head>
<meta charset="utf-8">
<title>Walking anew: a gentle recovery companion – cover spread</title>
<link href="https://fonts.googleapis.com/css2?family=Oswald:wght@500;600&family=Roboto+Condensed:wght@700&family=Roboto:wght@400&display=swap" rel="stylesheet">
<style>
  :root{
    --bg:#ececec;
    --paper:#ffffff;
    --paper-shade:#f3f4f6;
    --blue:#4a86cf;
    --blue-light:#6fb0e6;
    --blue-deep:#3c73b8;
    --ink-blue:#3a6fb5;
    --art-light:#dfe8f6;
    --art-mid:#a9bfe6;
    --art-deep:#7f9ad6;
    --photo-top:#c9b8a6;
    --photo-bottom:#e9e6e2;
    --white:#ffffff;
  }
  *{margin:0;padding:0;box-sizing:border-box}
  html,body{width:1200px;height:800px;overflow:hidden;background:var(--bg)}
  .spread{position:absolute;left:180px;top:105px;width:840px;height:590px;display:flex;box-shadow:0 10px 30px rgba(0,0,0,.12)}
  .page{position:relative;width:420px;height:590px;background:linear-gradient(90deg,var(--paper),var(--paper-shade));overflow:hidden}
  .page--front{background:linear-gradient(90deg,var(--paper-shade),var(--paper) 12%)}
  .band{position:absolute;left:0;width:100%;background:linear-gradient(180deg,var(--blue-light),var(--blue))}
  .back .band--top{top:0;height:92px}
  .back .band--bottom{top:525px;height:38px}
  .front .band--top{top:0;height:92px}
  .front .band--bottom{top:525px;height:38px;width:210px}
  .front .band--tab{top:525px;height:38px;left:410px;width:10px}

  .portrait{position:absolute;left:140px;top:162px;width:143px;height:172px;border:3px solid var(--blue);border-radius:10px;background:linear-gradient(180deg,var(--photo-top),var(--photo-bottom))}

  .brand{position:absolute;display:flex;align-items:center;gap:6px;font-family:Roboto,Arial,sans-serif;color:var(--ink-blue);white-space:nowrap}
  .brand__mark{flex:none;border-radius:50%;border:2.5px solid var(--blue)}
  .brand__text{display:flex;flex-direction:column;line-height:1.1}
  .back .brand{left:152px;top:350px}
  .back .brand__mark{width:24px;height:24px}
  .back .brand__name{font-size:12px}
  .back .brand__sub{font-size:8.5px}
  .front .brand{left:218px;top:525px;height:38px}
  .front .brand__mark{width:34px;height:34px;border-width:3px}
  .front .brand__name{font-size:17px}
  .front .brand__sub{font-size:12px}

  .copy{position:absolute;font-family:"Roboto Condensed","Arial Narrow",sans-serif;font-weight:700;color:var(--ink-blue)}
  .back .copy{left:77px;top:390px;width:270px;font-size:8.6px;line-height:1.22;text-align:justify;text-align-last:center}
  .front .copy--top{left:18px;top:22px;width:390px;font-size:10.5px;line-height:1.25;text-align:center;color:var(--white)}
  .front .copy--side{left:226px;top:368px;width:184px;font-size:10.5px;line-height:1.25;text-align:justify;text-align-last:right}

  .hip-art{position:absolute;left:0;top:92px;width:210px;height:433px;background:radial-gradient(ellipse at 45% 55%,var(--art-deep),var(--art-mid) 45%,var(--art-light) 80%,var(--paper) 100%)}

  .title-box{position:absolute;left:183px;top:148px;width:237px;height:148px;border-radius:6px 0 0 6px;background:linear-gradient(180deg,var(--blue-light),var(--blue-deep));color:var(--white);font-family:Oswald,"Arial Narrow",sans-serif;font-size:0;text-align:center;display:flex;flex-direction:column;justify-content:center;align-items:center}
  .title-box__main{display:block;font-size:31px;font-weight:600;line-height:1.08;letter-spacing:.3px;text-transform:uppercase}
  .title-box__rule{display:block;width:206px;height:2px;background:var(--white);margin:8px 0 6px}
  .title-box__sub{display:block;font-size:17px;font-weight:500;line-height:1.15;text-transform:uppercase;letter-spacing:.3px}
</style>
</head>
<body>
<main class="spread">
  <section class="page back" aria-label="Back cover">
    <div class="band band--top"></div>
    <div class="portrait" role="img" aria-label="Portrait photograph of the surgeon in a white coat"></div>
    <div class="brand">
      <span class="brand__mark"></span>
      <span class="brand__text"><span class="brand__name">Dr. Caio R. Duarte</span><span class="brand__sub">Cirurgia do Quadril</span></span>
    </div>
    <p class="copy">Lorem ipsum dolor sit amet, consectetur adipisicing elit, sed do eiusmod tempor incididunt ut labore et dolore magna aliqua. Ut enim ad minim veniam, quis nostrud exercitation. Lorem ipsum dolor sit amet, consectetur adipisicing elit, sed do eiusmod tempor incididunt ut labore et dolore magna aliqua. Ut enim ad minim veniam, quis nostrud exercitation. Lorem ipsum dolor sit amet, consectetur adipisicing elit, sed do eiusmod tempor incididunt ut labore et dolore magna aliqua. Ut enim ad minim veniam, quis nostrud exercitation.</p>
    <div class="band band--bottom"></div>
  </section>

  <section class="page page--front front" aria-label="Front cover">
    <div class="band band--top"></div>
    <p class="copy copy--top">Lorem ipsum dolor sit amet, consectetur adipisicing elit, sed do eiusmod tempor incididunt ut labore et dolore magna aliqua. Ut enim ad minim veniam, quis nostrud exercitation.</p>
    <div class="hip-art" role="img" aria-label="Blue-toned illustration of a hip joint with a prosthetic implant"></div>
    <h1 class="title-box">
      <span class="title-box__main">Walking<br>anew</span>
      <span class="title-box__rule"></span>
      <span class="title-box__sub">A gentle recovery<br>companion</span>
    </h1>
    <p class="copy copy--side">Lorem ipsum dolor sit amet, consectetur adipisicing elit, sed do eiusmod tempor incididunt ut labore et dolore magna aliqua. Ut enim ad minim veniam, quis nostrud exercitation.</p>
    <div class="band band--bottom"></div>
    <div class="brand">
      <span class="brand__mark"></span>
      <span class="brand__text"><span class="brand__name">Dr. Caio R. Duarte</span><span class="brand__sub">Cirurgia do Quadril</span></span>
    </div>
    <div class="band band--tab"></div>
  </section>
</main>
</body>
</html>
```